Business card

would like a double sided business card made up with my logos provided.
Prefer card to have black background and to use the black logos, with matching blue writing for the text.
One side to just be the logo, (Try to use both the black logos)
the other side to have the logo and also my credentials/business information.

Covering all aspects of Carpentry and Building Services

Marcus Tolvey
Qualified Carpenter
Mob: 0417263948
Email: rkt.joinery@mailbright.com
ABN: 47 615 209 834

Industry/Entity Type

Business

Contact Information for Business Card

Marcus Tolvey
Qualified Carpenter
Mob: 0417263948
ABN: 47 615 209 834

Requirements
Must have
• Please try to use both the black logos and incorporate into the card.

```html
<!DOCTYPE html>
<html lang="en">
<head>
<meta charset="utf-8">
<title>RKT Joinery – Business Card</title>
<link rel="stylesheet" href="https://fonts.googleapis.com/css2?family=Raleway:wght@400;500;600;700&display=swap">
<style>
  :root {
    --canvas: #e9e7e3;
    --card-dark: #161618;
    --card-mid: #2b2b2e;
    --blue: #2eaee0;
    --blue-deep: #1b93c4;
    --white: #ffffff;
    --grey-text: #d9d9d9;
  }
  * { box-sizing: border-box; margin: 0; padding: 0; }
  html, body {
    width: 1200px; height: 1000px; overflow: hidden;
    background: var(--canvas);
    font-family: "Raleway", sans-serif;
  }
  .card {
    position: absolute; left: 240px;
    width: 720px; height: 440px;
    border-radius: 6px; overflow: hidden;
    background: linear-gradient(125deg, var(--card-mid) 0%, var(--card-dark) 45%, #0c0c0d 100%);
    box-shadow: 0 12px 30px rgba(0,0,0,.25);
  }
  .card--front { top: 40px; }
  .card--back { top: 520px; }

  /* front side */
  .top-strip {
    position: absolute; left: 0; top: 0; width: 100%; height: 12px;
    background: var(--blue);
  }
  .brand {
    position: absolute; display: flex; align-items: center; gap: 10px;
    color: var(--white); font-weight: 600; letter-spacing: 1px;
  }
  .brand__mark { background: var(--blue); }
  .card--front .brand { left: 40px; top: 62px; font-size: 28px; }
  .card--front .brand__mark { width: 22px; height: 22px; }

  .person { position: absolute; right: 40px; top: 68px; text-align: right; }
  .person__name { color: var(--white); font-weight: 700; font-size: 32px; }
  .person__role { color: var(--blue); font-weight: 500; font-size: 18px; margin-top: 4px; }

  .divider {
    position: absolute; left: 30px; right: 40px; top: 160px; height: 2px;
    background: var(--white);
  }

  .contacts { position: absolute; left: 40px; top: 192px; list-style: none; }
  .contacts li {
    display: flex; align-items: center; gap: 14px;
    color: var(--grey-text); font-size: 21px; font-weight: 400;
    height: 40px;
  }
  .contact-icon {
    width: 30px; height: 30px; border-radius: 5px;
    background: var(--blue);
    display: flex; align-items: center; justify-content: center;
    color: var(--white); font-size: 10px; font-weight: 700;
  }
  .contact-icon svg { width: 18px; height: 18px; }

  .service-band {
    position: absolute; left: 0; right: 0; bottom: 0; height: 62px;
    background: linear-gradient(90deg, var(--blue-deep), var(--blue));
    border-top-right-radius: 30px;
    display: flex; align-items: center; padding-left: 40px;
    color: var(--white); font-weight: 700; font-size: 19px; letter-spacing: .5px;
    text-transform: uppercase;
  }

  /* back side */
  .card--back .brand {
    left: 0; right: 0; top: 150px; justify-content: center;
    font-size: 60px; gap: 18px; letter-spacing: 3px;
  }
  .card--back .brand__mark { width: 40px; height: 40px; }
  .tagline {
    position: absolute; left: 0; right: 0; bottom: 40px; text-align: center;
    color: var(--blue); font-weight: 700; font-size: 20px; letter-spacing: .5px;
    text-transform: uppercase;
  }
</style>
</head>
<body>

<section class="card card--front" aria-label="Business card, contact side">
  <div class="top-strip"></div>

  <div class="brand">
    <span class="brand__mark"></span>
    <span class="brand__name">RKT JOINERY</span>
  </div>

  <div class="person">
    <p class="person__name">Marcus Tolvey</p>
    <p class="person__role">Qualified Carpenter</p>
  </div>

  <div class="divider"></div>

  <ul class="contacts">
    <li>
      <span class="contact-icon">
        <svg viewBox="0 0 18 18" fill="none" stroke="#fff" stroke-width="1.6">
          <rect x="5" y="2" width="8" height="14" rx="1.5"/>
          <line x1="8" y1="13.5" x2="10" y2="13.5"/>
        </svg>
      </span>
      <span>0417263948</span>
    </li>
    <li>
      <span class="contact-icon">
        <svg viewBox="0 0 18 18" fill="none" stroke="#fff" stroke-width="1.6">
          <rect x="2" y="4" width="14" height="10" rx="1"/>
          <polyline points="2,4 9,10 16,4"/>
        </svg>
      </span>
      <span>rkt.joinery@mailbright.com</span>
    </li>
    <li>
      <span class="contact-icon">ABN</span>
      <span>47 615 209 834</span>
    </li>
  </ul>

  <div class="service-band">Covering all aspects of carpentry and building services</div>
</section>

<section class="card card--back" aria-label="Business card, logo side">
  <div class="brand">
    <span class="brand__mark"></span>
    <span class="brand__name">RKT JOINERY</span>
  </div>
  <p class="tagline">Covering all aspects of carpentry and building services</p>
</section>

</body>
</html>
```